Piano Tuning Company Needs a Postcard Design to Advertise Online Appointments

I need a postcard design for my piano tuning company. I help maintain my client's piano by tuning and doing minor repairs to increase the joy of playing their instrument. My website is now set up to book appointments online and I would like to offer $10 off of any service for making an appointment from our website, valid for 2014 only. The online booking application allows customers to see all openings on the calendar for the service they are looking for and sidesteps playing phone tag to set up an appointment. I would like to see designs that go well with the logo and its color scheme. The final design should communicate warmth, professionalism and a desire to maintain their beautiful instrument.

Target Market(s)

People who own pianos

Industry/Entity Type

It Company

Requirements
Must have
• lunaridgecrafts@brindlemail.net
• (425) 736-1905
• Try our online booking service and receive $10 off any service
• Offer only valid for 2014
Nice to have
• Definitely picture(s) of pianos. I have attached one that is also on my business card, but if a different picture(s) work better for your design, please feel free to use it.
• It might be nice to have something about "avoid playing phone tag, try our online service." Or there could be something about a piano needing to be tuned once a year, and when was the last time your piano was tuned?

```html
<!DOCTYPE html>
<html lang="en">
<head>
<meta charset="utf-8">
<title>Luna Ridge Tuning – Postcard</title>
<link rel="stylesheet" href="https://fonts.googleapis.com/css2?family=Cinzel:wght@400;700&family=Italianno&display=swap">
<style>
  :root {
    --white: #ffffff;
    --magenta: #e4117e;
    --pink-soft: #f4b6d6;
    --violet: #6a12c8;
    --violet-deep: #4b1a86;
    --ink: #111111;
    --grey: #5a5a5a;
  }
  * { margin: 0; padding: 0; box-sizing: border-box; }
  html, body { width: 1200px; height: 776px; overflow: hidden; background: var(--white); }
  .postcard { position: relative; width: 1200px; height: 776px; background: var(--white); overflow: hidden; }

  .brand { position: absolute; left: 50px; top: 130px; display: flex; align-items: center; gap: 24px; }
  .brand-dot { width: 40px; height: 40px; border-radius: 50%; background: var(--magenta); }
  .brand-name {
    font-family: "Cinzel", serif; font-weight: 700; font-size: 72px;
    color: var(--violet-deep); letter-spacing: 1px; line-height: 1; white-space: nowrap;
  }

  .contact-band {
    position: absolute; left: 0; top: 195px; width: 1200px; height: 135px;
    background: linear-gradient(to bottom, var(--white) 0%, var(--pink-soft) 30%, #b25ad6 62%, var(--violet) 100%);
  }
  .contact-line {
    position: absolute; left: 0; width: 100%; text-align: center;
    font-family: "Cinzel", serif; font-weight: 700; color: var(--white);
    font-size: 24px; letter-spacing: 2px; white-space: nowrap; line-height: 1;
  }
  .contact-line.web { top: 64px; word-spacing: 18px; }
  .contact-line.phone { top: 94px; }
  .band-rule { position: absolute; left: 0; top: 330px; width: 1200px; height: 7px; background: var(--magenta); }

  .divider { position: absolute; left: 700px; top: 337px; width: 6px; height: 328px; background: var(--magenta); }

  .message { position: absolute; left: 20px; top: 350px; width: 670px; text-align: center; }
  .service-line {
    font-family: "Cinzel", serif; font-size: 27px; letter-spacing: 4px;
    color: var(--ink); line-height: 32px; white-space: nowrap;
  }
  .tagline {
    font-family: "Italianno", cursive; font-size: 118px; line-height: 92px;
    color: var(--magenta); margin-top: 26px; white-space: nowrap;
  }
  .cta {
    font-family: "Cinzel", serif; font-size: 27px; letter-spacing: 4px;
    color: var(--ink); margin-top: 18px; white-space: nowrap;
  }

  .offer { position: absolute; left: 0; top: 688px; width: 1200px; text-align: center; }
  .offer-line {
    font-family: "Cinzel", serif; font-weight: 700; font-size: 21px;
    letter-spacing: 2px; color: var(--grey); line-height: 30px; white-space: nowrap;
  }
  .offer-line strong { color: var(--magenta); }
</style>
</head>
<body>
  <main class="postcard">
    <header class="brand">
      <span class="brand-dot" aria-hidden="true"></span>
      <span class="brand-name">Luna Ridge Tuning</span>
    </header>

    <section class="contact-band">
      <p class="contact-line web">www.lunaridgetuning.com lunaridgecrafts@brindlemail.net</p>
      <p class="contact-line phone">Phone: (425) 736-1905</p>
    </section>
    <div class="band-rule"></div>

    <section class="message">
      <p class="service-line">Offering exceptional service in<br>tuning and minor piano repair.</p>
      <p class="tagline">Let us get you back to<br>tickeling the ivories!</p>
      <p class="cta">Call or schedule online today!</p>
    </section>

    <div class="divider"></div>

    <section class="offer">
      <p class="offer-line">Try our online booking service and receive <strong>$10 off</strong> any service</p>
      <p class="offer-line">Offer only valid for 2014</p>
    </section>
  </main>
</body>
</html>
```